Business Card Design Project For Moving Company

Hello,

We need the business card to be 2 sided and we were thinking to use the logo on the front of the card (see file 1 attached) and the text "logo" (see file 2 attached) in the back of the card. We're looking for a powerful design that will help us build our brand, as our company is new.
We are a full service moving company (no storage) located in San Diego, CA, USA. The design should communicate to our potential customers that we have the highest level of service, customer satisfaction is our number one goal, our team is professional and efficient.

Thank you,

Dorn
Updates

Project Deadline Extended
Reason: We would like to have more time to provide feedback for the designs already submitted. Thank you, Dorn

Industry/Entity Type

Moving Company

Requirements
Must have
• Front of the card must have the following text and logo:
Haulbright, Inc
Residential And Commercial
Local And Long Distance
Address: 7312 Quillmont Rd, #146,
San Diego, CA, 92784
P: 855-372-LIFT (5438)
F: 858-529-4407
info@haul-bright.com
www.haul-bright.com

Back of the card must have the following text and text "logo" (file 2 attached):

The best compliment we can ever receive is a referral from our clients.

```html
<!DOCTYPE html>
<html lang="en">
<head>
<meta charset="utf-8">
<title>Haulbright, Inc – Business Card</title>
<link href="https://fonts.googleapis.com/css2?family=Anton&family=Arimo:ital,wght@0,400;0,700;1,400&display=swap" rel="stylesheet">
<style>
  :root {
    --red: #e21f26;
    --ink: #231f20;
    --paper: #ffffff;
    --stage: #ececec;
    --card-shade: #f1f1f1;
    --figure: #3a3a3a;
  }
  * { margin: 0; padding: 0; box-sizing: border-box; }
  html, body { width: 1200px; height: 1000px; overflow: hidden; background: var(--paper); }
  .canvas { position: relative; width: 1200px; height: 1000px; background: var(--paper); font-family: "Arimo", Arial, sans-serif; color: var(--ink); }

  .accent-band { position: absolute; left: 1060px; width: 140px; background: var(--red); }
  .accent-band--top { top: 0; height: 500px; }
  .accent-band--bottom { top: 940px; height: 60px; }

  .brand-mark { position: absolute; top: 188px; left: 0; width: 1200px; text-align: center; padding-right: 0; }
  .brand-mark__name { font-family: "Anton", Impact, sans-serif; font-size: 112px; line-height: 1; letter-spacing: 1px; color: var(--ink); margin-left: 0; }

  .card-stage { position: absolute; top: 500px; left: 0; width: 1200px; height: 440px; background: var(--stage); }

  .card { position: absolute; top: 80px; width: 490px; height: 280px; background: linear-gradient(135deg, var(--paper) 0%, var(--card-shade) 100%); box-shadow: 0 6px 18px rgba(0,0,0,.18); overflow: hidden; }
  .card--front { left: 73px; }
  .card--back { left: 637px; }

  .card-front__name { position: absolute; left: 28px; top: 34px; font-family: "Anton", Impact, sans-serif; font-size: 46px; line-height: 1; color: var(--red); letter-spacing: .5px; }
  .card-front__inc { position: absolute; left: 290px; top: 30px; font-size: 11px; font-weight: 700; color: var(--ink); }
  .card-front__services { position: absolute; left: 30px; top: 98px; font-size: 12px; font-weight: 700; line-height: 15px; color: var(--red); }
  .card-front__contact { position: absolute; left: 270px; top: 98px; font-size: 11.5px; line-height: 15px; list-style: none; }
  .card-front__contact li { display: flex; gap: 10px; }
  .card-front__label { width: 10px; font-weight: 700; color: var(--red); }
  .card-front__address { position: absolute; left: 30px; top: 206px; font-size: 11.5px; line-height: 15px; font-style: normal; }

  .card-back__figure { position: absolute; left: 24px; top: 40px; width: 120px; height: 200px; }
  .card-back__quote-band { position: absolute; left: 150px; right: 0; top: 135px; height: 105px; background: var(--red); display: flex; align-items: center; padding: 0 26px; }
  .card-back__quote { color: var(--paper); font-size: 15px; line-height: 21px; font-style: italic; }
</style>
</head>
<body>
<main class="canvas">
  <div class="accent-band accent-band--top"></div>
  <div class="accent-band accent-band--bottom"></div>

  <header class="brand-mark">
    <span class="brand-mark__name">HAULBRIGHT</span>
  </header>

  <section class="card-stage">
    <article class="card card--front">
      <div class="card-front__name">HAULBRIGHT</div>
      <div class="card-front__inc">Inc</div>
      <p class="card-front__services">Residential And Commercial<br>Local And Long Distance</p>
      <ul class="card-front__contact">
        <li><span class="card-front__label">P</span>855-372-LIFT (5438)</li>
        <li><span class="card-front__label">F</span>858-529-4407</li>
        <li><span class="card-front__label">E</span>info@haul-bright.com</li>
        <li><span class="card-front__label">W</span>www.haul-bright.com</li>
      </ul>
      <address class="card-front__address">7312 Quillmont Rd, #146,<br>San Diego, CA, 92784</address>
    </article>

    <article class="card card--back">
      <svg class="card-back__figure" role="img" aria-label="Lettermark illustration of two movers in dark and red" viewBox="0 0 120 200">
        <rect width="120" height="200" fill="var(--figure)"/>
      </svg>
      <div class="card-back__quote-band">
        <p class="card-back__quote">“The best compliment we can<br>ever receive is a referral from<br>our clients”</p>
      </div>
    </article>
  </section>
</main>
</body>
</html>
```